Personal Development Brand Needs a Workbook Cover Design

We need a clean and sleek cover design for our A4-Sized workbook called the "Lantern Path Journal Set"

There's around 90 pages in the workbook, if that matters for the spine.

Necessary Elements on the Front Cover:

- Logo
- Title: Keen Crest Lantern Path Journal
- Subtitle: A Simple Workbook to Track Your Transformation
- Author Name: Dorian Pellow

Elements on Back Cover:

- The Keen Crest Charter

```html
<!DOCTYPE html>
<html lang="en">
<head>
<meta charset="utf-8">
<title>Keen Crest Lantern Path Journal – Cover</title>
<link href="https://fonts.googleapis.com/css2?family=Archivo+Black&family=Oranienbaum&display=swap" rel="stylesheet">
<style>
  :root {
    --backdrop: #2b2a2a;
    --paper: #e9e9e7;
    --rule-grey: #a9a9a9;
    --brand-red: #d23a2c;
    --navy: #232c3b;
    --cream: #f3ecc0;
    --deep-blue: #0d2440;
    --mid-blue: #2f73b0;
    --ink-black: #1b1b1b;
  }
  * { margin: 0; padding: 0; box-sizing: border-box; }
  html, body {
    width: 1200px; height: 909px; overflow: hidden;
    background: var(--backdrop);
  }
  .stage {
    width: 1200px; height: 909px;
    display: flex; align-items: center; justify-content: center;
  }
  .cover {
    position: relative;
    width: 580px; height: 820px;
    background: var(--deep-blue);
    overflow: hidden;
  }
  .brand-band {
    position: absolute; left: 0; top: 0; width: 100%; height: 150px;
    background: var(--paper);
    display: flex; align-items: center; justify-content: center;
  }
  .brand-name {
    font-family: "Archivo Black", sans-serif;
    font-size: 64px; color: var(--navy);
    letter-spacing: -1px;
  }
  .grey-rule {
    position: absolute; left: 0; top: 150px; width: 100%; height: 14px;
    background: var(--rule-grey);
  }
  .title-band {
    position: absolute; left: 0; top: 164px; width: 100%; height: 96px;
    background: var(--brand-red);
    display: flex; align-items: center; justify-content: center;
  }
  .title {
    font-family: "Oranienbaum", serif;
    font-weight: 400; font-size: 42px; color: var(--cream);
    transform: scaleX(0.82);
    white-space: nowrap;
  }
  .artwork {
    position: absolute; left: 0; top: 260px; width: 100%; height: 560px;
    background: radial-gradient(ellipse at 50% 30%, var(--mid-blue) 0%, #174a7c 40%, var(--deep-blue) 85%);
  }
  .subtitle {
    position: absolute; left: 0; top: 300px; width: 100%;
    font-family: "Oranienbaum", serif;
    font-size: 34px; line-height: 1.15; color: var(--cream);
    text-align: center;
  }
  .corner-shapes {
    position: absolute; left: 0; top: 0; width: 580px; height: 820px;
  }
  .author {
    position: absolute; right: 40px; top: 700px;
    font-family: "Archivo Black", sans-serif;
    font-size: 30px; color: var(--brand-red);
  }
</style>
</head>
<body>
  <main class="stage">
    <section class="cover">
      <header class="brand-band">
        <span class="brand-name">Keen Crest</span>
      </header>
      <div class="grey-rule"></div>
      <div class="title-band">
        <h1 class="title">Keen Crest Lantern Path Journal</h1>
      </div>
      <div class="artwork" role="img" aria-label="Blue digital illustration of a wireframe head with circuit lines"></div>
      <p class="subtitle">A Simple Workbook to<br>Track Your Transformation</p>
      <svg class="corner-shapes" viewBox="0 0 580 820" aria-hidden="true">
        <polygon points="580,420 580,820 250,820 240,690" fill="var(--ink-black)"/>
        <polygon points="150,600 240,690 250,820 60,820 60,700" fill="var(--brand-red)"/>
      </svg>
      <p class="author">Dorian Pellow</p>
    </section>
  </main>
</body>
</html>
```